Trim Path Studio needs A4 information sheets that vibrant and easy to read with a healthy food...

I have written an introduction an "About Me " and 4 pages of material that will be uploaded on my website "Trim Path Studio" but I am not a designer and it looks boring. I need the information to remain unchanged but the presentation to look better, The logo was designed through Artboard Hive. The text could be moew interesting, Introduction page has NO …… NO...… etc these could be scattered or high lighted. There could be healthy food symbols in the margins etc

Colors
3176b5
add136
fbf286

Requirements
Must have
• The content must not be changed just the presentation.
Nice to have
• Colour . Symbols of foods such as fruits, vegetables, fish , seafood ,
Should not have
• Any high fat foods , fast foods,
• NO REFERENCE TO GYMS OR EXCERCISE THIS IS JUST ABOUT FOOD.

```html
<!DOCTYPE html>
<html lang="en">
<head>
<meta charset="utf-8">
<title>Trim Path Studio – Information Sheet</title>
<link href="https://fonts.googleapis.com/css2?family=Oswald:wght@500;700&family=Open+Sans:ital,wght@0,400;0,600;0,700;1,400;1,600&display=swap" rel="stylesheet">
<style>
:root{
  --orange:#f26a22;
  --green:#add136;
  --green-dark:#7fa51e;
  --blue:#3176b5;
  --yellow:#fbf286;
  --panel:#fdf8d2;
  --ink:#3a3a3a;
  --white:#ffffff;
}
*{box-sizing:border-box;margin:0;padding:0}
html,body{width:849px;height:1200px;overflow:hidden;background:var(--white)}
body{font-family:"Open Sans",Arial,sans-serif;color:var(--ink);position:relative}
.header{position:absolute;left:0;top:0;width:849px;height:80px;background:var(--orange);display:flex;align-items:center;justify-content:center}
.header h1{font-family:"Oswald",Arial,sans-serif;font-weight:700;color:var(--white);font-size:46px;letter-spacing:1px}
.intro{position:absolute;left:150px;top:95px;width:549px;font-size:14px;line-height:1.45;font-style:italic;font-weight:600;color:var(--ink);text-align:center}
.no-list{position:absolute;left:0;top:150px;width:849px;height:290px}
.no-item{position:absolute;width:200px;text-align:center;font-size:13px;line-height:1.35}
.no-item b{display:block;color:var(--ink);font-weight:600}
.no-icon{width:60px;height:60px;border-radius:50%;border:3px solid var(--green-dark);margin:0 auto 10px;display:flex;align-items:center;justify-content:center}
.no-icon span{width:28px;height:28px;border-radius:50%;background:var(--green)}
.no-item.wide{width:320px}
.truth-band{position:absolute;left:0;top:470px;width:849px;height:70px;background:var(--green);color:var(--white);font-size:15px;line-height:1.4;text-align:center;display:flex;align-items:center;justify-content:center;padding:0 70px;font-weight:600}
.panel{position:absolute;left:34px;top:556px;width:781px;height:420px;background:var(--panel);border:3px solid var(--orange);padding:16px 34px}
.panel h2{font-family:"Oswald",Arial,sans-serif;font-weight:700;color:var(--blue);font-size:40px;text-align:center;letter-spacing:1px;line-height:1.2}
.panel .lead{color:var(--blue);font-weight:600;font-size:15px;text-align:center;margin:4px 30px 14px;line-height:1.35}
.purchase{display:flex;align-items:center;gap:18px;color:var(--blue);font-weight:600;font-size:14.5px;line-height:1.35;margin-bottom:14px}
.eat-bar{background:var(--orange);color:var(--white);font-size:13px;font-weight:600;padding:6px 14px;margin-bottom:12px}
.ticks{list-style:none;padding-left:40px}
.ticks li{display:flex;gap:14px;font-size:13.5px;line-height:1.45;margin-bottom:11px}
.ticks svg{flex:0 0 20px;margin-top:1px}
.personal{position:absolute;left:42px;top:1000px;width:765px;color:var(--blue);font-weight:600;font-size:14.5px;line-height:1.4;text-transform:uppercase;text-align:center}
.brand{position:absolute;left:34px;top:1085px;display:flex;align-items:center;gap:8px}
.brand i{width:30px;height:30px;border-radius:50%;background:var(--green);display:block}
.brand span{font-family:"Open Sans",Arial,sans-serif;font-weight:700;color:var(--green-dark);font-size:15px;width:90px;line-height:1.15}
.action-band{position:absolute;left:150px;top:1128px;width:699px;height:48px;background:var(--green);color:var(--white);font-family:"Oswald",Arial,sans-serif;font-weight:500;font-size:20px;display:flex;align-items:center;justify-content:center;letter-spacing:.5px}
</style>
</head>
<body>
<header class="header"><h1>TRIM PATH STUDIO</h1></header>
<p class="intro">A Dietitian with 40 years of experience, gives you the SIMPLE TRUTH about how to lose weight, the easy way.</p>

<section class="no-list">
  <div class="no-item" style="left:40px;top:12px">
    <div class="no-icon" role="img" aria-label="Weighing scale icon"><span></span></div>
    <b>NO weighing</b>or measuring
  </div>
  <div class="no-item" style="left:325px;top:12px">
    <div class="no-icon" role="img" aria-label="Calculator icon"><span></span></div>
    <b>NO counting calories,</b>carbs, points, protein
  </div>
  <div class="no-item" style="left:600px;top:12px">
    <div class="no-icon" role="img" aria-label="Pills and shake icon"><span></span></div>
    <b>NO "step trackers" or</b>"medications, or "shakes"
  </div>
  <div class="no-item wide" style="left:30px;top:150px">
    <div class="no-icon" role="img" aria-label="Swimwear icon"><span></span></div>
    <b>NO group therapy, blogs, tweeting, forums,</b>psychotherapy, bikini challenges or 6 pack challenges
  </div>
  <div class="no-item wide" style="left:470px;top:150px">
    <div class="no-icon" role="img" aria-label="Apple and seeds icon"><span></span></div>
    <b>NO Kale, Chia, Apple cider</b>Vinegar, or avoidance of gluten !
  </div>
</section>

<div class="truth-band">Learn the simple truth and clear instructions that work. Thousands of people have benefitted and changed their lives forever.</div>

<section class="panel">
  <h2>HOW DOES THIS SITE WORK?</h2>
  <p class="lead">WATCH A SHORT VIDEO WHERE MAREN SHARES WITH YOU THE WAY SHE HAS HELPED THOUSANDS OF PEOPLE LOSE WEIGHT.</p>
  <div class="purchase">
    <svg width="46" height="30" viewBox="0 0 46 30" aria-hidden="true"><rect x="1" y="4" width="44" height="22" rx="2" fill="var(--green)"/><circle cx="23" cy="15" r="6" fill="var(--white)"/></svg>
    <p>PURCHASE WITH A ONCE ONLY PAYMENT OF $99 THEN DOWNLOAD THE SIMPLE WRITTEN MATERIALS YOU NEED:</p>
  </div>
  <div class="eat-bar">"What you can eat" (Abundant choice of foods that YOU like and suit your taste and your budget)</div>
  <ul class="ticks">
    <li><svg width="20" height="18" viewBox="0 0 20 18" aria-hidden="true"><path d="M2 9l6 6L18 2" fill="none" stroke="var(--green-dark)" stroke-width="3"/></svg><p>"Foods to avoid". Most of these are foods that can be eaten occasionally such as a weekend meal out or a celebration.</p></li>
    <li><svg width="20" height="18" viewBox="0 0 20 18" aria-hidden="true"><path d="M2 9l6 6L18 2" fill="none" stroke="var(--green-dark)" stroke-width="3"/></svg><p>"Shopping list". Supermarkets are part of life now. While they contain thousands of foods that cause overweight and obesity they also have fantastic foods that make life simple and losing weight easy.</p></li>
    <li><svg width="20" height="18" viewBox="0 0 20 18" aria-hidden="true"><path d="M2 9l6 6L18 2" fill="none" stroke="var(--green-dark)" stroke-width="3"/></svg><p>4 week menu that does not require you to be a TV celebrity chef.</p></li>
    <li><svg width="20" height="18" viewBox="0 0 20 18" aria-hidden="true"><path d="M2 9l6 6L18 2" fill="none" stroke="var(--green-dark)" stroke-width="3"/></svg><p>Recipes. You can choose to live on. Simple, quick and easy meals.</p></li>
  </ul>
</section>

<p class="personal">A personal link will be sent to your giving you access to another video with Maren where she will go through the materials and help you understand how you can eat in the way that suits your lifestyle.</p>

<div class="brand"><i></i><span>Trim Path Studio</span></div>
<div class="action-band">TAKE ACTION NOW AND BEGIN A NEW LIFE OF OPTIMISM HEALTH AND VITALITY</div>
</body>
</html>
```